Freelancer Information Security professional needs a business card

I need a simple, young, elegant business card. I'm a freelancer in the InfoSec area and want to be able to give my card to potential customers and new people I meet.

I'd like to have a clean, professional look but at same time not boring or corporate.

The only requirement is to have my "introduction" phrase which is:
"Half hacker, half mercenary."

I have added a card I have as a example, which I think it gives a good example of style I want.

Target Market(s)

Technology / Computers / Engineering

Industry/Entity Type

Information Technology

Contact Information for Business Card

Contact fields I want included:

(351) 93 708 12 54
tomas@vornel.im
https://vornel.im

Font styles to use
Sans Serif

Requirements
Nice to have
• Card doesn't need to have a doubled side, but it looks good / fits the design then please do include.
Should not have
• Outdated graphics or images; too much patterns/colors.

```html
<!DOCTYPE html>
<html lang="en">
<head>
<meta charset="utf-8">
<title>Tomas — InfoSec Freelancer Business Card</title>
<link rel="stylesheet" href="https://fonts.googleapis.com/css2?family=Arimo:wght@400;700&display=swap">
<style>
  :root {
    --page-bg: #2b2b2d;
    --card-top: #ffffff;
    --card-bottom: #e4e4e4;
    --brand-blue: #1a8fde;
    --ink: #0d0d0d;
    --on-blue: #ffffff;
    --on-blue-soft: #cfe7f8;
  }
  html, body {
    margin: 0;
    width: 1200px;
    height: 997px;
    overflow: hidden;
    background: var(--page-bg);
    font-family: "Arimo", Arial, sans-serif;
  }
  .card {
    position: absolute;
    left: 150px;
    top: 241px;
    width: 900px;
    height: 514px;
    border-radius: 34px;
    background: linear-gradient(160deg, var(--card-top) 0%, var(--card-bottom) 100%);
    overflow: hidden;
  }
  .edge-band {
    position: absolute;
    left: 0; top: 0; bottom: 0;
    width: 46px;
    background: var(--brand-blue);
  }
  .edge-line {
    position: absolute;
    left: 64px; top: 0; bottom: 0;
    width: 11px;
    background: var(--brand-blue);
  }
  .intro {
    position: absolute;
    left: 108px;
    top: 62px;
    line-height: 1;
  }
  .intro .greeting {
    display: block;
    font-size: 92px;
    color: var(--ink);
    letter-spacing: -1px;
  }
  .intro .name {
    display: block;
    font-size: 104px;
    color: var(--brand-blue);
    margin-top: -4px;
    letter-spacing: -1px;
  }
  .intro .role {
    display: block;
    font-size: 60px;
    color: var(--ink);
    margin-top: 4px;
  }
  .intro .field {
    display: block;
    font-size: 40px;
    color: var(--brand-blue);
    letter-spacing: 2px;
    margin-top: 2px;
  }
  .contact-box {
    position: absolute;
    left: 594px;
    top: 42px;
    width: 276px;
    height: 252px;
    border-radius: 12px;
    background: var(--brand-blue);
    box-sizing: border-box;
    padding: 16px 18px 0 18px;
    text-align: right;
  }
  .contact-box .label {
    display: block;
    font-size: 15px;
    color: var(--ink);
    letter-spacing: 1px;
  }
  .contact-box .value {
    display: block;
    font-size: 22px;
    color: var(--on-blue);
    margin: 8px 0 22px;
    white-space: nowrap;
  }
  .motto-bar {
    position: absolute;
    left: 108px;
    top: 412px;
    width: 762px;
    height: 52px;
    border-radius: 10px;
    background: var(--brand-blue);
    color: var(--on-blue-soft);
    font-size: 28px;
    letter-spacing: 5px;
    text-align: center;
    line-height: 52px;
    text-transform: uppercase;
  }
</style>
</head>
<body>
  <div class="card">
    <div class="edge-band"></div>
    <div class="edge-line"></div>

    <div class="intro">
      <span class="greeting">Hi,I’m</span>
      <span class="name">Tomas</span>
      <span class="role">FREELANCER</span>
      <span class="field">in the InfoSec area</span>
    </div>

    <div class="contact-box">
      <span class="label">PHONE</span>
      <span class="value">(351) 93 708 12 54</span>
      <span class="label">EMAIL</span>
      <span class="value">tomas@vornel.im</span>
      <span class="label">WEBSITE</span>
      <span class="value">https://vornel.im</span>
    </div>

    <div class="motto-bar">Half hacker, half&nbsp; mercenary</div>
  </div>
</body>
</html>
```